Custom Canvas Design

Attached is photo of customers truck and their company logo. We are looking at getting this printed onto a canvas for a Christmas gift.

We do want some nice writing below stated:
"We are grateful for your partnership this year. Thank you for sticking with us!"

Design we would like to see:
Try making the photo more 3D cartoony style

Target Market(s)

Cartoon/3D

Font styles to use
Script

Requirements
Should not have
• No Christmas items or theme.

```html
<!DOCTYPE html>
<html lang="en">
<head>
<meta charset="utf-8">
<title>Thank You – Harlow Haulage</title>
<link rel="stylesheet" href="https://fonts.googleapis.com/css2?family=Montserrat:wght@600;700&family=Roboto+Condensed:wght@700&family=Great+Vibes&family=Roboto:wght@400&display=swap">
<style>
  :root {
    --page: #ffffff;
    --brand-red: #b40000;
    --deep-red: #9c0000;
    --white: #ffffff;
    --gold: #fff200;
    --ink: #222222;
  }
  * { box-sizing: border-box; margin: 0; padding: 0; }
  html, body { width: 926px; height: 1200px; overflow: hidden; background: var(--page); }
  .card {
    position: absolute; left: 62px; top: 58px; width: 802px; height: 1090px;
    background: var(--brand-red); overflow: hidden;
  }
  .brand-badge {
    position: absolute; left: 305px; top: 82px; width: 192px; height: 192px;
    border-radius: 50%; background: var(--white);
    display: flex; align-items: center; justify-content: center; text-align: center;
  }
  .brand-name {
    font-family: "Montserrat", sans-serif; font-weight: 700; font-size: 22px;
    line-height: 1.15; color: var(--deep-red); letter-spacing: 1px;
  }
  .headline { font-weight: normal; }
  .headline-small {
    position: absolute; left: 0; width: 100%; top: 325px; text-align: center;
    font-family: "Montserrat", sans-serif; font-weight: 600; font-size: 31px;
    line-height: 38px; color: var(--white); letter-spacing: 2px;
  }
  .headline-large {
    position: absolute; left: 0; width: 100%; top: 365px; text-align: center;
    font-family: "Montserrat", sans-serif; font-weight: 600; font-size: 64px;
    line-height: 78px; color: var(--white); letter-spacing: 1px;
  }
  .partnership-line {
    position: absolute; left: 0; width: 100%; top: 466px; text-align: center;
    font-family: "Roboto Condensed", sans-serif; font-weight: 700; font-size: 27px;
    line-height: 34px; color: var(--gold); letter-spacing: 0.3px;
  }
  .sticking-line {
    position: absolute; left: 0; width: 100%; top: 512px; text-align: center;
    font-family: "Great Vibes", cursive; font-size: 62px; line-height: 74px;
    color: var(--white);
  }
  .sticking-end {
    position: absolute; left: 0; width: 100%; top: 584px; text-align: center;
    font-family: "Great Vibes", cursive; font-size: 66px; line-height: 78px;
    color: var(--gold);
  }
  .truck-illustration { position: absolute; left: 0; top: 700px; width: 802px; height: 390px; }
  .site-address {
    position: absolute; right: 28px; top: 818px;
    font-family: "Roboto", sans-serif; font-size: 15px; color: var(--ink);
  }
</style>
</head>
<body>
  <main class="card">
    <div class="brand-badge">
      <span class="brand-name">HARLOW<br>HAULAGE</span>
    </div>

    <h1 class="headline">
      <span class="headline-small">HEARTFELT</span>
      <span class="headline-large">THANKS</span>
    </h1>
    <p class="partnership-line">WE ARE GRATEFUL FOR YOUR PARTNERSHIP THIS YEAR.</p>
    <p class="sticking-line">Thank you for sticking</p>
    <p class="sticking-end">with us!</p>

    <svg class="truck-illustration" viewBox="0 0 802 390" role="img" aria-label="3D cartoon-style illustration of the customer's white prime mover towing a low loader carrying an orange excavator">
      <defs>
        <linearGradient id="sceneTone" x1="0" y1="0" x2="0" y2="1">
          <stop offset="0" stop-color="#c9ccd0"/>
          <stop offset="0.45" stop-color="#e4e5e6"/>
          <stop offset="0.75" stop-color="#c2c4c6"/>
          <stop offset="1" stop-color="#8a8d90"/>
        </linearGradient>
      </defs>
      <rect width="802" height="390" fill="url(#sceneTone)"/>
      <path d="M0 0 H802 V60 C700 60 620 70 540 100 C440 135 300 155 160 140 C90 132 40 120 0 112 Z" fill="#ffffff"/>
    </svg>

    <p class="site-address">www.northridgeprints.com.au</p>
  </main>
</body>
</html>
```